High Quality Business card for Property Management Agency - Super Classy and professional design

High Quality Business card design.

We need a business card designed for our Property Management Agency.
We are located on Sydney's Northern Beaches and manage beautiful properties along the beach and harbor.
We need a design that oozes modern, classy and professional.
I would like it to be double sided with contact details and logo on the front and just the logo on the back.

I need a print ready PDF version of the file as well as an editable photoshop (PSD) version of the file.

Logo and information details attached.

Target Market(s)

Property owners/investors, Male and Female Aged 28-65

Industry/Entity Type

Real Estate

Contact Information for Business Card

Tom Carrick
Tel: 0467 239 018
Email: tom@harvestlaneestates.com.au
Website: www.harvestlaneestates.com.au
Address: Level 2, 17 Wattlecourt Rd, Dunmarra NSW 2187

Font styles to use
Sans Serif

Requirements
Must have
• - Logo front and back
• - Business card details listed above and attached
• - Colour
Nice to have
• Sleek and professional

```html
<!DOCTYPE html>
<html lang="en">
<head>
<meta charset="utf-8">
<title>Harvest Lane Estates – Business Card</title>
<link rel="stylesheet" href="https://fonts.googleapis.com/css2?family=Source+Sans+3:wght@400;600;700&display=swap">
<style>
  :root {
    --backdrop: #1c1c1c;
    --card-white: #f3f3f3;
    --ink: #1a1a1a;
    --teal: #1a8a96;
    --teal-light: #2aa0a8;
    --teal-dark: #127a88;
    --white: #ffffff;
  }
  * { margin: 0; padding: 0; box-sizing: border-box; }
  html, body {
    width: 1200px;
    height: 900px;
    overflow: hidden;
  }
  body {
    background: var(--backdrop);
    font-family: "Source Sans 3", sans-serif;
    position: relative;
  }
  .card {
    position: absolute;
    top: 184px;
    height: 490px;
    border-radius: 12px;
    overflow: hidden;
  }
  .card-front {
    left: 299px;
    width: 301px;
    background: var(--card-white);
    color: var(--ink);
    text-align: center;
  }
  .card-back {
    left: 645px;
    width: 304px;
    background: linear-gradient(180deg, var(--teal-light) 0%, var(--teal) 55%, var(--teal-dark) 100%);
  }
  .wordmark {
    position: absolute;
    top: 276px;
    left: 0;
    right: 0;
    top: 90px;
    display: flex;
    align-items: center;
    justify-content: center;
    gap: 8px;
  }
  .wordmark-dot {
    width: 12px;
    height: 12px;
    border-radius: 50%;
    background: var(--teal);
  }
  .wordmark-name {
    font-size: 22px;
    font-weight: 700;
    letter-spacing: 0.2px;
    color: var(--ink);
  }
  .contact {
    position: absolute;
    top: 302px;
    left: 0;
    right: 0;
  }
  .contact-name {
    font-size: 19px;
    font-weight: 600;
    color: var(--teal);
    margin-bottom: 14px;
  }
  .contact-address,
  .contact-lines {
    font-size: 13.5px;
    line-height: 20px;
  }
  .contact-address { margin-bottom: 13px; }
  .back-name {
    position: absolute;
    left: 0;
    right: 0;
    top: 405px;
    text-align: center;
    font-size: 25px;
    font-weight: 600;
    color: var(--white);
    letter-spacing: 0.2px;
  }
</style>
</head>
<body>
  <section class="card card-front">
    <div class="wordmark">
      <span class="wordmark-dot"></span>
      <span class="wordmark-name">HARVEST LANE ESTATES</span>
    </div>
    <div class="contact">
      <p class="contact-name">Tom Carrick</p>
      <p class="contact-address">Level 2, 17 Wattlecourt Rd,<br>Dunmarra NSW 2187</p>
      <p class="contact-lines">0467 239 018<br>tom@harvestlaneestates.com.au<br>www.harvestlaneestates.com.au</p>
    </div>
  </section>

  <section class="card card-back" role="img" aria-label="Teal card back with a faint large brand mark decoration">
    <p class="back-name">HARVEST LANE ESTATES</p>
  </section>
</body>
</html>
```